DOG DAYCARE BILLBOARD

Design a bold exciting billboard that can be read easily from a distance! Our goal is brand awareness and showcasing the services we offer (Boarding, Grooming, Daycare, and Training.
we would like to see examples with the phrase "your best friend's best day". Our name Bright Meadow Canine Activity Center (or just Bright Meadow might work better and could be bigger) and the services we provide.
(there are two examples of what we like included in the pictures)
you can find more information o our website at pawplayhub@mailnest.example.

```html
<!DOCTYPE html>
<html lang="en">
<head>
<meta charset="utf-8">
<title>Bright Meadow Billboard</title>
<link rel="stylesheet" href="https://fonts.googleapis.com/css2?family=Exo+2:ital,wght@1,800&family=Jost:wght@400;700&display=swap">
<style>
  :root {
    --olive: #c2b72f;
    --white: #ffffff;
    --ink: #1b1b1b;
    --paper: #ffffff;
    --frame: #2a2a2a;
  }
  * { margin: 0; padding: 0; box-sizing: border-box; }
  html, body { width: 1200px; height: 1200px; overflow: hidden; background: var(--paper); }
  .canvas { position: relative; width: 1200px; height: 1200px; }
  .billboard {
    position: absolute; left: 89px; top: 92px; width: 1026px; height: 472px;
    background: var(--white); border: 1px solid var(--frame); overflow: hidden;
    font-family: "Jost", sans-serif;
  }
  .band-top { position: absolute; left: 0; top: 0; width: 100%; height: 140px; background: var(--olive); }
  .band-bottom { position: absolute; left: 0; bottom: 0; width: 100%; height: 91px; background: var(--olive); }
  .brand-mark {
    position: absolute; left: 26px; top: 56px; display: flex; align-items: center; gap: 8px;
    font-weight: 700; font-size: 16px; color: var(--ink);
    text-transform: uppercase; letter-spacing: 0.5px; white-space: nowrap;
  }
  .brand-mark .dot { width: 14px; height: 14px; border-radius: 50%; background: var(--ink); }
  .brand-name {
    position: absolute; left: 266px; top: 42px;
    font-family: "Exo 2", sans-serif; font-style: italic; font-weight: 800;
    font-size: 64px; line-height: 1; color: var(--white); letter-spacing: 11px;
    text-transform: uppercase; white-space: nowrap;
  }
  .photo-left {
    position: absolute; left: 35px; top: 244px; width: 360px; height: 137px;
    background: radial-gradient(ellipse at 50% 80%, #3a2a1f 0%, #a8652f 35%, #c98a4a 70%, #ffffff 100%);
    border-radius: 45% 45% 0 0;
  }
  .photo-right {
    position: absolute; left: 731px; top: 112px; width: 276px; height: 272px;
    background: radial-gradient(ellipse at 50% 45%, #6d6d6d 0%, #bdb8b2 40%, #e9e6e2 75%, #ffffff 100%);
    border-radius: 40% 40% 10% 10%;
  }
  .tagline {
    position: absolute; left: 41px; top: 168px; z-index: 1;
    font-weight: 700; font-size: 39px; line-height: 1; color: var(--ink); letter-spacing: 0;
    white-space: nowrap;
  }
  .services { position: absolute; left: 421px; top: 232px; list-style: none; z-index: 1; }
  .services li {
    display: flex; align-items: center; gap: 14px; height: 33.7px;
    font-weight: 700; font-size: 28px; color: var(--ink); letter-spacing: 0.3px; white-space: nowrap;
  }
  .services li::before {
    content: ""; width: 20px; height: 20px; border-radius: 50%; background: var(--olive); flex: none;
  }
  .phone {
    position: absolute; left: 0; bottom: 0; width: 100%; height: 91px;
    display: flex; align-items: center; justify-content: center; gap: 14px; color: var(--white);
  }
  .phone .label { font-weight: 400; font-size: 42px; }
  .phone .number { font-weight: 700; font-size: 58px; letter-spacing: 1px; }
</style>
</head>
<body>
<div class="canvas">
  <section class="billboard">
    <div class="band-top"></div>
    <div class="band-bottom"></div>

    <div class="brand-mark"><span class="dot"></span><span>Bright Meadow</span></div>
    <h1 class="brand-name">Bright Meadow</h1>

    <div class="photo-left" role="img" aria-label="Photo of a brown and tan dog peeking over the bottom edge"></div>
    <div class="photo-right" role="img" aria-label="Photo of a smiling fawn French bulldog with a red collar, paws over the edge"></div>

    <h2 class="tagline">YOUR BEST FRIEND’S BEST DAY</h2>

    <ul class="services">
      <li>DOG BOARDING</li>
      <li>DOG GROOMING</li>
      <li>DOG DAYCARE</li>
      <li>DOG TRAINING</li>
    </ul>

    <div class="phone">
      <span class="label">Call:</span>
      <span class="number">(555) 284 - 0163</span>
    </div>
  </section>
</div>
</body>
</html>
```